Vocational Mentor needs an impressive business card

1. I need a business card (or maybe three with identic look) to promote me and my three business titles/services:
- Vocational Mentor. I help people find their vocation and live happily from it. I use my 20 years of experience in business, management and psychology to help them identify the most efficient ways to make a living doing what they are passionate about.
- Business Angel. I help founders start a succesful business with minimum risks and costs. I use my 20 years of experience in sales, management and entrepreneurship to help them identify the most efficient ways, in terms of time and cost, to validate their business idea.
- Learning Designer. I design unique learning programs that produce long-term cognitive and behavioural changes to people and organisations. I use my 20 years of experience in learning, teaching and change management to create minimalist experiences and processes that allow them to change efficiently in their pursued direction.

2. I would like a two-sided business card, on the front with my name, contact details and titles, on the back the explanation of the services.
Updates

Hi all,

I updated my brief, included contacts info and give feedback on all designs I got. I am new on this platform so please tell me if you need anything else or if I don't use corectly the platform forms.

Kind regards,
Mirel

Hi all,

I shortened the services description by deleting the phrase "I call..."

Kind regards,
Mirel

Target Market(s)

Freelancers, startups, people and organization willing to invest in change through ultimate learning experiences

Industry/Entity Type

Business

Font styles to use
Serif

Requirements
Must have
• Front side: full name, titles, web site, email, phone like below:
Mirel Vantaru
Vocational Mentor, Business Angel, Learning Designer
info@mirelvantaru.example
www.mirelvantaru.example
+40-748-MIRELV
Nice to have
• Back side: the description of the services I provide as in the task description.
1/3: it would be nice if I can jam all three titles on the front side but then I need a solution to jam all three services on the back side.

```html
<!DOCTYPE html>
<html lang="en">
<head>
<meta charset="utf-8">
<title>Mirel Vantaru – Business Card</title>
<link rel="stylesheet" href="https://fonts.googleapis.com/css2?family=Questrial&display=swap">
<style>
  :root {
    --slate: #525963;
    --slate-light: #5e6977;
    --slate-dark: #434b55;
    --paper: #ffffff;
    --accent-green: #93c154;
    --title-green: #a6c75e;
    --title-yellow: #ece74a;
    --title-orange: #d9693e;
    --ink-white: #ffffff;
    --body-blue: #a7b6c8;
    --rule: #2f353c;
  }
  * { box-sizing: border-box; margin: 0; padding: 0; }
  html, body {
    width: 982px; height: 1200px; overflow: hidden;
    background: var(--paper);
    font-family: "Questrial", "Century Gothic", sans-serif;
  }
  .canvas { position: relative; width: 982px; height: 1200px; }

  /* Front side */
  .card-front {
    position: absolute; left: 0; top: 0; width: 982px; height: 545px;
    background: var(--slate);
  }
  .side-tab {
    position: absolute; top: 140px; width: 13px; height: 288px;
    background: var(--accent-green);
  }
  .side-tab--left { left: 0; border-radius: 0 6px 6px 0; }
  .side-tab--right { right: 0; border-radius: 6px 0 0 6px; }

  .identity {
    position: absolute; right: 500px; top: 196px; text-align: right;
  }
  .identity__name {
    font-size: 40px; font-weight: 400; color: var(--ink-white);
    letter-spacing: 1px; line-height: 52px; margin-right: 20px;
  }
  .identity__titles { list-style: none; margin-top: 12px; margin-right: 18px; }
  .identity__titles li { font-size: 32px; line-height: 37px; }
  .title--mentor { color: var(--title-green); }
  .title--angel { color: var(--title-yellow); }
  .title--designer { color: var(--title-orange); }

  .divider {
    position: absolute; left: 498px; top: 145px; width: 2px; height: 275px;
  }

  .contact {
    position: absolute; left: 514px; top: 262px; list-style: none;
    color: var(--ink-white); font-size: 24px; line-height: 38.5px;
  }

  /* Back side */
  .card-back {
    position: absolute; left: 0; top: 655px; width: 982px; height: 545px;
  }
  .service {
    position: absolute; left: 0; width: 982px; text-align: center;
  }
  .service--mentor { top: 0; height: 180px; background: var(--slate-light); padding-top: 22px; }
  .service--angel { top: 180px; height: 175px; background: var(--slate); padding-top: 12px; }
  .service--designer { top: 355px; height: 190px; background: var(--slate-dark); padding-top: 12px; }
  .service__heading {
    font-size: 27px; font-weight: 700; letter-spacing: 0.5px; line-height: 34px;
    -webkit-text-stroke: 0.6px currentColor;
  }
  .service--mentor .service__heading { color: var(--title-green); margin-bottom: 12px; }
  .service--angel .service__heading { color: var(--title-yellow); margin-bottom: 6px; }
  .service--designer .service__heading { color: var(--title-orange); margin-bottom: 4px; }
  .service__text {
    font-size: 21px; line-height: 23.5px; color: var(--body-blue);
  }
</style>
</head>
<body>
<main class="canvas">
  <section class="card-front" aria-label="Front side">
    <span class="side-tab side-tab--left"></span>
    <span class="side-tab side-tab--right"></span>

    <div class="identity">
      <h1 class="identity__name">MIREL VANTARU</h1>
      <ul class="identity__titles">
        <li class="title--mentor">Vocational Mentor</li>
        <li class="title--angel">Business Angel</li>
        <li class="title--designer">Learning Designer</li>
      </ul>
    </div>

    <svg class="divider" viewBox="0 0 2 275" aria-hidden="true">
      <line x1="1" y1="0" x2="1" y2="275" stroke="var(--rule)" stroke-width="1.5" stroke-dasharray="3 3"/>
    </svg>

    <ul class="contact">
      <li>phone: +40-748-MIRELV</li>
      <li>email: info@mirelvantaru.example</li>
      <li>site: www.mirelvantaru.example</li>
    </ul>
  </section>

  <section class="card-back" aria-label="Back side">
    <article class="service service--mentor">
      <h2 class="service__heading">VOCATIONAL MENTOR</h2>
      <p class="service__text">I help people find their vocation and live happily from it. I use my 20 years of<br>experience in business, management and psychology to help them identify the<br>most efficient ways to make a living doing what they are passionate about.</p>
    </article>
    <article class="service service--angel">
      <h2 class="service__heading">BUSINESS ANGEL</h2>
      <p class="service__text">I help founders start a succesful business with minimum risks and costs.<br>I use my 20 years of experience in sales, management and entrepreneurship<br>to help them identify the most efficient ways, in terms of time and cost,<br>to validate their business idea.</p>
    </article>
    <article class="service service--designer">
      <h2 class="service__heading">LEARNING DESIGNER</h2>
      <p class="service__text">I design unique learning programs that produce long-term cognitive and<br>behavioural changes to people and organisations. I use my 20 years of<br>experience in learning, teaching and change management to create<br>minimalist experiences and processes that allow them to change efficiently<br>in their pursued direction.</p>
    </article>
  </section>
</main>
</body>
</html>
```